Marlow's Wiring (www.marlowswiring.example)

I own and operate a telecommunication business in Dallas, Texas. We specialize in Ethernet cabling , networking, wireless implementation, security camera (CCTV) installation, Home theater systems, Audio/Video installations, Lighting

i would like a full vehicle wrap for the Vantor Roadmaster R310 Cargo Van
i will attach our company logo PDF so it can be added as well.
I am looking for a modern, sleek logo with Bold letters. i want it to scream luxury service.
please emphasize " 5 star rated on Findly and Rateo" somehow, include "CTB A+ Rated" and Or the CTB A+ logo which i will include a photo of it.
I will also attach ideas of the van designs i like from the internet. i am open to changing my business colors so feel free to suggest new logo design/colors.
No Cartoon characters or people in van design.
i would like for the van wrap to include a few key words similar to the "clear line" Van design on each side of the van wrap. Keywords can be: Network wiring | Audio | Video | Surveillance | Wi-Fi

please include my phone number 555 013 2468
and my website Marlowswiring.example

Vehicle wrap company image Requirements:
Create or convert all layered files to RGB Color Mode in Adobe Photoshop CS3 or Adobe Illustrator CS3. Do not use CMYK Color Mode.

Assign Adobe RGB (1998) Color Profile to both bitmap and vector-formatted files.

Send vector files as true vector files.

A bitmap image such as a .JPG or .TIF file, saved as an .EPS/.AI file in a vector program, such as Adobe Illustrator, does not constitute as being true vector.

Design all layered files at actual print size at 72 dpi, with at least 6” of extra bleed beyond vehicle outline.

Supplied art files must be in high resolution. If you are unsure of the resolution of an image, play it safe and always go big! The higher the resolution in dots per inch (dpi) and the bigger the dimensions, the less chance of the image(s) will have of pixelation.

Do not resize art files down for uploading purposes. Instead, compress all files, individually

```html
<!DOCTYPE html>
<html lang="en">
<head>
<meta charset="utf-8">
<title>Marlow's Wiring – Van Wrap</title>
<link rel="stylesheet" href="https://fonts.googleapis.com/css2?family=Montserrat:wght@500;600;700;800&display=swap">
<style>
  :root {
    --brand-blue: #1c8fd6;
    --brand-cyan: #2cc3ea;
    --ink: #2b2f36;
    --wrap-white: #f7f9fb;
    --cable-dark: #0f2a44;
    --cable-mid: #2a7fbf;
    --cable-light: #5ec0ee;
    --tire: #1b1d20;
    --rim: #c9cdd2;
    --trim: #b8bcc2;
    --glass: #8a9097;
    --tail: #a3121a;
    --badge: #1f5fae;
    --page: #ffffff;
  }
  * { box-sizing: border-box; margin: 0; padding: 0; }
  html, body { width: 1200px; height: 1200px; overflow: hidden; background: var(--page); }
  body { font-family: "Montserrat", sans-serif; }
  .canvas { position: relative; width: 1200px; height: 1200px; }
  .van-art { position: absolute; inset: 0; }
  .txt { position: absolute; white-space: nowrap; line-height: 1; }

  .side-name { left: 568px; top: 100px; font-size: 54px; font-weight: 700; color: var(--brand-blue); letter-spacing: 1px; }
  .side-name-sub { left: 658px; top: 160px; font-size: 28px; font-weight: 700; color: var(--brand-blue); letter-spacing: 7px; }
  .side-keywords { left: 498px; top: 206px; font-size: 21px; font-weight: 600; color: var(--ink); letter-spacing: 0.5px; }
  .side-web { left: 504px; top: 302px; font-size: 24px; font-weight: 600; color: #fff; }
  .side-phone { left: 502px; top: 336px; font-size: 44px; font-weight: 700; color: #fff; letter-spacing: 1px; }

  .review { position: absolute; color: var(--brand-blue); font-weight: 700; }
  .review .count { display: block; font-size: 13px; text-align: right; color: var(--brand-blue); }
  .review .name { display: block; font-size: 46px; line-height: 0.95; }
  .review .score { display: block; font-size: 13px; letter-spacing: 1px; }
  .side-review { left: 298px; top: 284px; width: 172px; }

  .rear-name { left: 408px; top: 724px; width: 404px; text-align: center; font-size: 44px; font-weight: 700; color: var(--brand-blue); letter-spacing: 1px; }
  .rear-name-sub { left: 408px; top: 774px; width: 404px; text-align: center; font-size: 23px; font-weight: 700; color: var(--brand-blue); letter-spacing: 6px; }
  .rear-web { left: 408px; top: 828px; font-size: 17px; font-weight: 600; color: #fff; }
  .rear-phone { left: 406px; top: 850px; font-size: 26px; font-weight: 700; color: #fff; letter-spacing: 1px; }
  .rear-review { left: 472px; top: 914px; width: 130px; }
  .rear-review .name { font-size: 32px; }
  .rear-review .count, .rear-review .score { font-size: 10px; }
</style>
</head>
<body>
<div class="canvas">
  <svg class="van-art" width="1200" height="1200" viewBox="0 0 1200 1200">
    <defs>
      <linearGradient id="cable-fill" x1="0" y1="0" x2="0" y2="1">
        <stop offset="0" stop-color="var(--cable-dark)"/>
        <stop offset="0.35" stop-color="var(--cable-mid)"/>
        <stop offset="0.7" stop-color="var(--cable-light)"/>
        <stop offset="1" stop-color="var(--cable-dark)"/>
      </linearGradient>
      <clipPath id="side-body">
        <path d="M40 270 L60 232 L200 212 L290 110 Q305 70 340 66 L1150 66 Q1170 68 1172 90 L1178 380 Q1180 410 1160 412 L40 412 Q26 410 26 390 Z"/>
      </clipPath>
      <clipPath id="rear-body">
        <path d="M360 600 Q370 578 410 576 L808 576 Q848 578 858 600 L880 830 L880 985 L338 985 L338 830 Z"/>
      </clipPath>
    </defs>

    <!-- side view -->
    <g class="side-view">
      <g clip-path="url(#side-body)">
        <rect x="20" y="60" width="1170" height="360" fill="var(--wrap-white)"/>
        <path d="M20 258 Q120 246 220 256 T420 250 T640 256 T860 248 T1190 254 L1190 420 L20 420 Z" fill="url(#cable-fill)" role="img" aria-label="Photo of bundled blue network cables plugged into a patch panel"/>
      </g>
      <path d="M290 110 L300 210 L468 210 L468 110 Q468 98 456 98 L310 98 Z" fill="var(--glass)"/>
      <rect x="40" y="276" width="30" height="56" rx="4" fill="var(--trim)"/>
      <rect x="22" y="340" width="80" height="38" rx="6" fill="var(--trim)"/>
      <rect x="1128" y="250" width="18" height="60" rx="3" fill="var(--tail)"/>
      <rect x="1126" y="360" width="58" height="40" rx="5" fill="var(--trim)"/>
      <rect x="574" y="92" width="0" height="0"/>
      <rect x="1128" y="100" width="0" height="0"/>
      <rect x="946" y="96" width="110" height="110" rx="14" fill="var(--brand-cyan)" class="brand-square"/>
      <rect x="1018" y="282" width="104" height="78" rx="8" fill="var(--badge)" class="rating-badge"/>
      <g class="wheel">
        <circle cx="190" cy="414" r="70" fill="var(--tire)"/>
        <circle cx="190" cy="414" r="42" fill="var(--rim)"/>
        <circle cx="190" cy="414" r="14" fill="#8d9298"/>
      </g>
      <g class="wheel">
        <circle cx="948" cy="414" r="70" fill="var(--tire)"/>
        <circle cx="948" cy="414" r="42" fill="var(--rim)"/>
        <circle cx="948" cy="414" r="14" fill="#8d9298"/>
      </g>
    </g>

    <!-- rear view -->
    <g class="rear-view">
      <rect x="350" y="560" width="518" height="20" rx="10" fill="var(--trim)"/>
      <rect x="572" y="566" width="74" height="12" rx="3" fill="var(--tail)"/>
      <g clip-path="url(#rear-body)">
        <rect x="330" y="570" width="560" height="420" fill="var(--wrap-white)"/>
        <path d="M330 812 Q420 798 520 808 T700 804 T890 806 L890 990 L330 990 Z" fill="url(#cable-fill)" role="img" aria-label="Photo of bundled blue network cables plugged into a patch panel"/>
      </g>
      <line x1="609" y1="580" x2="609" y2="985" stroke="#c4c8cd" stroke-width="2"/>
      <rect x="340" y="822" width="44" height="90" rx="4" fill="var(--tail)"/>
      <rect x="834" y="822" width="44" height="90" rx="4" fill="var(--tail)"/>
      <rect x="636" y="840" width="120" height="62" rx="6" fill="#111"/>
      <rect x="564" y="600" width="96" height="96" rx="12" fill="var(--brand-cyan)" class="brand-square"/>
      <rect x="418" y="912" width="44" height="52" rx="5" fill="var(--badge)" class="rating-badge"/>
      <rect x="334" y="978" width="550" height="56" rx="10" fill="var(--trim)"/>
      <rect x="360" y="1034" width="70" height="94" rx="10" fill="var(--tire)"/>
      <rect x="788" y="1034" width="70" height="94" rx="10" fill="var(--tire)"/>
      <rect x="430" y="1040" width="358" height="30" fill="#3a3d42"/>
    </g>
  </svg>

  <!-- side texts -->
  <div class="txt side-name">MARLOW'S</div>
  <div class="txt side-name-sub">WIRING</div>
  <div class="txt side-keywords">Network wiring • Audio • Video • Surveillance • Wi-Fi</div>
  <div class="review side-review">
    <span class="count">50+ Reviews</span>
    <span class="name">Findly</span>
    <span class="score">5.0 ★★★★★</span>
  </div>
  <div class="txt side-web">marlowswiring.example</div>
  <div class="txt side-phone">555 013 2468</div>

  <!-- rear texts -->
  <div class="txt rear-name">MARLOW'S</div>
  <div class="txt rear-name-sub">WIRING</div>
  <div class="txt rear-web">marlowswiring.example</div>
  <div class="txt rear-phone">555 013 2468</div>
  <div class="review rear-review">
    <span class="count">50+ Reviews</span>
    <span class="name">Findly</span>
    <span class="score">5.0 ★★★★★</span>
  </div>
</div>
</body>
</html>
```